business cards, stationary, email signature
Professional
Greta Volsky
President
Corporate office:
3620 E Tamsin Road, Larkmont, CA 92814
Other locations in Bellhaven, CA and Corwin Falls, NV
greta@farwellgrp.net
www.farwellgrp.net
482650, K, D74
*8(a), *SDB, *SBE, *MBE, *DBE, *CBE
these certifications should be listed in the middle, bottom of the card.
■221119 – Other Electric Power Generation
■236210 – Industrial Building Construction
■236220 – Commercial and Institutional Building Construction
■237310 – Highway, Street, and Bridge Construction
■238160 – Roofing Contractors
■238170 – Siding Contractors
■238220 – Plumbing, Heating, and Air-Conditioning Contractors
■238310 – Drywall and Insulation Contractors
■238320 – Painting and Wall Covering Contractors
■238340 – Tile and Terrazzo Contractors
■238350 – Finish Carpentry Contractors
■238390 – Other Building Finishing Contractors
■238910 – Site Preparation Contractors
■238990 – All Other Specialty Trade Contractors
■541350 – Building Inspection Services
■561210 – Facilities Support Services
■561790 – Other Services to Buildings and Dwellings

```html
<!DOCTYPE html>
<html lang="en">
<head>
<meta charset="utf-8">
<title>Farwell Group – Business Card</title>
<link rel="stylesheet" href="https://fonts.googleapis.com/css2?family=Open+Sans:wght@400;600&display=swap">
<style>
  :root {
    --page: #efeae2;
    --card-light: #fffaf0;
    --card-warm: #f3e4c6;
    --navy: #0b1f5c;
    --blue: #1f5fd6;
    --blue-bright: #3a8cf0;
    --brand: #3b8fd0;
    --text-blue: #2f86c8;
    --text-dark: #3a3a3a;
    --badge: #f0a020;
  }
  * { box-sizing: border-box; margin: 0; padding: 0; }
  html, body { width: 1200px; height: 665px; overflow: hidden; }
  body {
    background: var(--page);
    font-family: "Open Sans", Arial, sans-serif;
    position: relative;
  }
  .card {
    position: absolute;
    top: 178px;
    width: 540px;
    height: 310px;
    background: radial-gradient(ellipse at 30% 35%, var(--card-light) 0%, var(--card-light) 40%, var(--card-warm) 100%);
    box-shadow: 0 6px 18px rgba(0,0,0,0.22);
    overflow: hidden;
  }
  .card--front { left: 40px; }
  .card--back { left: 620px; }

  .card-art { position: absolute; inset: 0; width: 100%; height: 100%; }

  .holder {
    position: absolute;
    top: 24px;
    right: 92px;
    text-align: right;
    color: #fff;
  }
  .holder-name { font-size: 15px; font-weight: 600; }
  .holder-title { font-size: 10px; opacity: 0.85; }

  .brand {
    position: absolute;
    left: 26px;
    top: 98px;
    display: flex;
    align-items: center;
    gap: 10px;
  }
  .brand-dot {
    width: 52px; height: 52px; border-radius: 50%;
    background: var(--badge);
  }
  .brand-name {
    font-size: 27px;
    font-weight: 400;
    letter-spacing: 1px;
    color: var(--brand);
    text-transform: uppercase;
  }
  .license {
    position: absolute;
    left: 88px;
    top: 140px;
    font-size: 9px;
    color: var(--text-blue);
  }

  .contact {
    position: absolute;
    right: 30px;
    top: 102px;
    list-style: none;
    text-align: right;
    font-size: 10px;
    line-height: 1.42;
    color: var(--text-blue);
  }
  .contact li { display: flex; justify-content: flex-end; align-items: center; gap: 6px; }
  .contact-icon { width: 7px; height: 7px; border-radius: 50%; background: var(--badge); }

  .office {
    position: absolute;
    left: 26px;
    top: 210px;
    font-size: 9.5px;
    line-height: 1.45;
    color: var(--text-blue);
  }
  .certs {
    position: absolute;
    left: 0; right: 0;
    bottom: 26px;
    text-align: center;
    font-size: 9.5px;
    color: var(--text-dark);
  }

  .codes {
    position: absolute;
    left: 30px;
    top: 18px;
    list-style: none;
    font-size: 9.6px;
    line-height: 1.5;
    color: var(--text-dark);
  }
  .codes li::before {
    content: "";
    display: inline-block;
    width: 5px; height: 5px;
    margin-right: 5px;
    background: var(--blue);
    vertical-align: middle;
  }
  .back-dot {
    position: absolute;
    right: 22px;
    bottom: 20px;
    width: 30px; height: 30px;
    border-radius: 50%;
    background: var(--badge);
  }
</style>
</head>
<body>

<section class="card card--front" aria-label="Business card front">
  <svg class="card-art" viewBox="0 0 540 310" preserveAspectRatio="none" aria-hidden="true">
    <defs>
      <linearGradient id="swoosh" x1="0" y1="0" x2="1" y2="0">
        <stop offset="0" stop-color="#0b1f5c"/>
        <stop offset="0.55" stop-color="#1f5fd6"/>
        <stop offset="1" stop-color="#3a8cf0"/>
      </linearGradient>
      <linearGradient id="curlFront" x1="0" y1="0" x2="1" y2="1">
        <stop offset="0" stop-color="#6d6d6d"/>
        <stop offset="0.6" stop-color="#1b1b1b"/>
        <stop offset="1" stop-color="#000"/>
      </linearGradient>
    </defs>
    <path class="swoosh" d="M270 0 H540 V78 C470 70 400 72 330 78 C300 80 280 60 270 0 Z" fill="url(#swoosh)"/>
    <path class="page-curl" d="M470 0 H540 V64 C520 40 498 14 470 0 Z" fill="url(#curlFront)"/>
  </svg>

  <div class="holder">
    <p class="holder-name">Greta Volsky</p>
    <p class="holder-title">President</p>
  </div>

  <div class="brand">
    <span class="brand-dot"></span>
    <span class="brand-name">Farwell Group</span>
  </div>
  <p class="license">License # 482650, K, D74</p>

  <ul class="contact">
    <li>(TF) 1.888.555.0142 <span class="contact-icon"></span></li>
    <li>T 1.714.555.0178 <span class="contact-icon"></span></li>
    <li>F 1.714.555.0193 <span class="contact-icon"></span></li>
    <li>M 1.714.555.0126 <span class="contact-icon"></span></li>
    <li>greta@farwellgrp.net <span class="contact-icon"></span></li>
    <li>marlow77 <span class="contact-icon"></span></li>
    <li>www.farwellgrp.net <span class="contact-icon"></span></li>
  </ul>

  <div class="office">
    <p>Corporate office:</p>
    <p>3620 E Tamsin Road, Larkmont, CA 92814</p>
    <p>Other locations in Bellhaven, CA and Corwin Falls, NV</p>
  </div>

  <p class="certs">Certifications: *8(a), *SDB, *SBE, *MBE, *DBE, *CBE</p>
</section>

<section class="card card--back" aria-label="Business card back">
  <svg class="card-art" viewBox="0 0 540 310" preserveAspectRatio="none" aria-hidden="true">
    <defs>
      <linearGradient id="curlBack" x1="1" y1="1" x2="0" y2="0">
        <stop offset="0" stop-color="#000"/>
        <stop offset="0.5" stop-color="#1b1b1b"/>
        <stop offset="1" stop-color="#6d6d6d"/>
      </linearGradient>
      <linearGradient id="swooshBack" x1="0" y1="0" x2="1" y2="0">
        <stop offset="0" stop-color="#1f5fd6"/>
        <stop offset="1" stop-color="#0b1f5c"/>
      </linearGradient>
    </defs>
    <path class="swoosh" d="M420 310 C440 270 480 240 540 225 V310 Z" fill="url(#swooshBack)"/>
    <path class="page-curl" d="M455 310 C470 280 500 250 540 232 V310 Z" fill="url(#curlBack)"/>
  </svg>

  <ul class="codes">
    <li>221119 – Other Electric Power Generation</li>
    <li>236210 – Industrial Building Construction</li>
    <li>236220 – Commercial and Institutional Building Construction</li>
    <li>237310 – Highway, Street, and Bridge Construction</li>
    <li>238160 – Roofing Contractors</li>
    <li>238170 – Siding Contractors</li>
    <li>238220 – Plumbing, Heating, and Air-Conditioning Contractors</li>
    <li>238310 – Drywall and Insulation Contractors</li>
    <li>238320 – Painting and Wall Covering Contractors</li>
    <li>238340 – Tile and Terrazzo Contractors</li>
    <li>238350 – Finish Carpentry Contractors</li>
    <li>238390 – Other Building Finishing Contractors</li>
    <li>238910 – Site Preparation Contractors</li>
    <li>238990 – All Other Specialty Trade Contractors</li>
    <li>541350 – Building Inspection Services</li>
    <li>561210 – Facilities Support Services</li>
    <li>561790 – Other Services to Buildings and Dwellings</li>
  </ul>
  <span class="back-dot"></span>
</section>

</body>
</html>
```